Vehcile and Personal GPS Tracking Service Needs Brochure

We need a brochure design for our serviced called Harbor Beacon Locate (HBL) www.harborbeaconlocate.com (info site) & www.harborbeaconlocate.net (our actually gps tracking site).

HBL provides a Live GPS Tracking service for vehicles and personal trackers (key tag size).

We need a brochure that will describe our products and its benefits.

The use of our product allows corporate companies to track their vehcile fleets and security their goods and vehciles.

Security is a big issues in our country. Car theif is common. Also, kidnapping of CEOs is a concern.

Our target audience are corporate companys, who are interested in managing their vehcile fleets and ensuring the security of their vehicles and staff memebers.

We would like to continue using the corporate colours of yellow and grey.

The design should communicate reliablity and safety.

Target Market(s)

Medium to large companies (10 or more vehciles). CEOs.

Industry/Entity Type

Security

Requirements
Must have
• Plese see the attached word document that we are providing customers.
Nice to have
• It would be good to have a picture of a vehcile being tracking on a map, so people have a visual of how it works.
Should not have
• The brouchure should not include pricing, as this may change. However, we would like to show that we hae to different rates for self montioring and security monitoring.

```html
<!DOCTYPE html>
<html lang="en">
<head>
<meta charset="utf-8">
<title>Harbor Beacon Locate – Tri-fold Brochure</title>
<link href="https://fonts.googleapis.com/css2?family=Josefin+Sans:wght@100&family=Quicksand:wght@400;500;700&display=swap" rel="stylesheet">
<style>
  :root {
    --panel-grey: #6b6b6e;
    --panel-grey-dark: #5b5b5e;
    --swoosh-grey: #8a8a8d;
    --brand-yellow: #f2c414;
    --brand-yellow-deep: #e0a90c;
    --paper: #ffffff;
    --ink: #4a4a4c;
    --label-grey: #8f8f8f;
  }
  html, body {
    margin: 0;
    padding: 0;
    width: 1200px;
    height: 618px;
    overflow: hidden;
    background: var(--paper);
  }
  .spread {
    position: relative;
    width: 1200px;
    height: 618px;
    font-family: "Quicksand", sans-serif;
  }
  .panel-label {
    position: absolute;
    top: 6px;
    width: 373px;
    text-align: center;
    font-family: "Josefin Sans", sans-serif;
    font-weight: 100;
    font-size: 46px;
    letter-spacing: 3px;
    color: var(--label-grey);
    line-height: 1;
  }
  .panel {
    position: absolute;
    top: 54px;
    width: 373px;
    height: 521px;
    overflow: hidden;
    background: var(--panel-grey);
    box-shadow: 0 6px 10px rgba(0,0,0,0.25);
  }
  .panel--flap { left: 38px; }
  .panel--back { left: 411px; }
  .panel--front { left: 784px; }
  .panel svg.panel-art {
    position: absolute;
    inset: 0;
  }

  /* Wordmark: single colour, single weight */
  .wordmark {
    position: absolute;
    color: var(--paper);
    font-weight: 700;
    text-align: center;
    line-height: 1.02;
    letter-spacing: 1px;
  }
  .wordmark-dot {
    position: absolute;
    border-radius: 50%;
    background: var(--brand-yellow);
  }

  /* Inside flap */
  .flap-wordmark {
    left: 8px;
    top: 52px;
    width: 120px;
    font-size: 13px;
  }
  .flap-dot { left: 55px; top: 16px; width: 28px; height: 28px; }
  .welcome {
    position: absolute;
    left: 27px;
    top: 226px;
    width: 330px;
    color: var(--ink);
  }
  .welcome-title {
    margin: 0 0 14px;
    font-size: 24px;
    font-weight: 400;
    color: var(--brand-yellow);
    letter-spacing: 0.5px;
  }
  .welcome p {
    margin: 0 0 13px;
    font-size: 10.6px;
    line-height: 13.6px;
    font-weight: 500;
  }

  /* Back */
  .back-dot { left: 167px; top: 150px; width: 40px; height: 40px; }
  .back-wordmark {
    left: 0;
    top: 232px;
    width: 373px;
    font-size: 34px;
  }
  .contact {
    position: absolute;
    left: 0;
    top: 369px;
    width: 373px;
    height: 152px;
    border-top: 3px solid var(--brand-yellow);
    border-bottom: 4px solid var(--brand-yellow);
    box-sizing: border-box;
    padding: 10px 12px 0;
    color: var(--paper);
  }
  .contact-title {
    margin: 0;
    font-size: 14.5px;
    font-weight: 500;
    color: var(--brand-yellow);
  }
  .contact-intro {
    margin: 1px 0 0;
    font-size: 10px;
    line-height: 12px;
    width: 320px;
  }
  .contact-name {
    margin: 14px 0 0;
    font-size: 14px;
  }
  .contact-role {
    margin: 0;
    font-size: 11px;
    font-style: italic;
    color: var(--brand-yellow);
  }
  .contact-lines {
    margin: 12px 0 0;
    font-size: 10px;
    line-height: 12.5px;
  }
  .contact-lines span { color: var(--brand-yellow); }
  .tracker-photo {
    position: absolute;
    right: 18px;
    bottom: 14px;
    width: 44px;
    height: 62px;
    border-radius: 16px;
    background: linear-gradient(160deg, #d02a2a, #7a1010 70%, #2b2b2b);
    transform: rotate(-18deg);
  }

  /* Front */
  .front-cta {
    position: absolute;
    left: 14px;
    top: 176px;
    width: 345px;
    text-align: center;
    color: var(--paper);
  }
  .front-cta-line {
    margin: 0;
    font-size: 8.6px;
    letter-spacing: 0.2px;
  }
  .front-url {
    margin: 4px 0 0;
    padding-bottom: 6px;
    border-bottom: 1.5px solid var(--brand-yellow);
    font-size: 21px;
    font-style: italic;
    letter-spacing: 0.8px;
  }
  .front-url span { color: var(--brand-yellow); }
  .front-dot { left: 161px; top: 300px; width: 50px; height: 50px; }
  .front-wordmark {
    left: 0;
    top: 400px;
    width: 373px;
    font-size: 34px;
  }
</style>
</head>
<body>
<main class="spread">

  <div class="panel-label" style="left:38px;">INSIDE FLAP</div>
  <div class="panel-label" style="left:411px;">BACK</div>
  <div class="panel-label" style="left:784px;">FRONT</div>

  <!-- Inside flap -->
  <section class="panel panel--flap">
    <svg class="panel-art" width="373" height="521" viewBox="0 0 373 521">
      <defs>
        <linearGradient id="dash-tone" x1="0" y1="0" x2="1" y2="1">
          <stop offset="0" stop-color="#2a3548"/>
          <stop offset="0.45" stop-color="#4b5566"/>
          <stop offset="1" stop-color="#1c1f25"/>
        </linearGradient>
      </defs>
      <rect width="373" height="521" fill="var(--panel-grey)"/>
      <path d="M100 0 H373 V280 C330 250 220 220 80 230 C80 150 90 60 100 0 Z" fill="url(#dash-tone)" role="img" aria-label="Photo of a car dashboard navigation screen showing a route map"/>
      <path d="M0 235 C120 175 270 190 373 262 V286 C270 222 120 210 0 262 Z" fill="var(--swoosh-grey)"/>
      <path d="M0 250 C120 200 270 215 373 285 V521 H0 Z" fill="var(--paper)"/>
    </svg>
    <div class="wordmark-dot flap-dot"></div>
    <div class="wordmark flap-wordmark">HARBOR BEACON LOCATE</div>
    <div class="welcome">
      <h2 class="welcome-title">Welcome</h2>
      <p>Welcome to Harbor Beacon Locate services.<br>Our website offers real time, live GPS tracking services.</p>
      <p>Using GPS satellite technology, Harbor Beacon Locate's service enables you to see a vehicle or person move on a computer screen in real time. This enables you to know precisely where the car or person is. Our car tracking service can be used to track at any type of a vehicle or a fleet of vehicles. Our hand held personal trackers can be carried by anyone.</p>
      <p>The tracking system can be accessed at any time from a computer in the privacy of your own office or home or on an internet mobile device (tablet or smart phone), enabling you to see a car's or person's path in real time. You do not need to purchase or install any special software on your computer – our service enables you to track a vehicle or person live from anywhere you have internet connection.</p>
    </div>
  </section>

  <!-- Back -->
  <section class="panel panel--back">
    <div class="wordmark-dot back-dot"></div>
    <div class="wordmark back-wordmark">HARBOR BEACON<br>LOCATE</div>
    <div class="contact">
      <h3 class="contact-title">Further Information &amp; Live Demonstration</h3>
      <p class="contact-intro">For further information on our services or a live demonstration on how our website works, please contact us:</p>
      <p class="contact-name">Reid Alcott</p>
      <p class="contact-role">Director</p>
      <p class="contact-lines"><span>Email:</span> reid@harborbeacon.co<br><span>Ph:</span> 418 2206</p>
      <div class="tracker-photo" role="img" aria-label="Photo of a red key-tag personal GPS tracker"></div>
    </div>
  </section>

  <!-- Front -->
  <section class="panel panel--front">
    <svg class="panel-art" width="373" height="521" viewBox="0 0 373 521">
      <rect width="373" height="521" fill="var(--panel-grey)"/>
      <path d="M0 95 C90 40 230 20 373 30 V0 H0 Z" fill="var(--panel-grey-dark)"/>
      <path d="M110 40 C190 10 290 0 373 0 V130 C340 70 250 45 110 40 Z" fill="var(--brand-yellow-deep)"/>
      <path d="M150 30 C220 8 300 0 373 0 V105 C335 55 260 35 150 30 Z" fill="var(--brand-yellow)"/>
    </svg>
    <div class="front-cta">
      <p class="front-cta-line">Subscribe to our services today, and start tracking your vehicles right away</p>
      <p class="front-url">www.<span>harborbeaconlocate</span>.com</p>
    </div>
    <div class="wordmark-dot front-dot"></div>
    <div class="wordmark front-wordmark">HARBOR BEACON<br>LOCATE</div>
  </section>

</main>
</body>
</html>
```